Wedding filmmaker needs artistic business card design - brightwaterreels.ca

We are high end wedding filmmakers in a major market who produce cinematic wedding films. We require a business card design that communicates our quality, artistry, and professionalism yet looks progressive and friendly. Colors and design should skew appeal more to the bride-to-be who is usually the decision maker but not be overtly feminine per se. This means generally light pastel shades of ivory, purple, pink, yellow, as examples.
We already have a name logo established: the words "Brightwater Reels" in the font Great Vibes. Designs must use Tallow natural cardstock as the print stock and am leaning heavily toward our name logo in white, but I am open to black as well. Please design any color elements with spot white underneath where possible.
Do not try to compliment or take inspiration from our website design. Treat the card design as a separate stand alone.
Thank you so much for your hard work!

Target Market(s)

Affluent couples spending $50,000+ on their wedding

Industry/Entity Type

Progressive

Contact Information for Business Card

Paul Brightwater
Producer
905-418-2937
www.brightwaterreels.ca
paul@brightwaterreels.ca
twitter @brightwater762

Font styles to use
Serif
Sans Serif

Requirements
Must have
• - Brightwater Reels name logo (reference GIF uploaded for reference only) and catch phrase: Breathtaking wedding films (I'm open to capitalizing all three words, or just first, or all in small caps). I favor logo, and catch phrase on front of card and my contact details on the other side but if you feel strongly about a different design, go for it!
• - Design must be submitted shown on Tallow natural cardstock NOT WHITE cardstock, If you're not familiar with Tallow, this is what it looks like: http://www.quillandtwinejournal.com/wp-content/uploads/2013/07/il_570xN.837264019_kq4m.jpg
Nice to have
• - An original graphic element (eg. movie reel, bouquet, confetti, etc.) that compliments the name logo but is subtle and discreet, doesn't overpower or entangle it.
• -Great use of balance, composition, negative space, etc. I like clean tasteful design
Should not have
• -Lousy boring clip art.
• -Graphic elements, fonts, or color palette from our website
• -White cardstock background
• -designs you have previously submitted for other contests
• -Bold dark colors (eg. red, orange navy blue, etc.)
• -High tech futuristic designs like you'd create for a software company

```html
<!DOCTYPE html>
<html lang="en">
<head>
<meta charset="utf-8">
<title>Brightwater Reels – Business Card</title>
<link rel="stylesheet" href="https://fonts.googleapis.com/css2?family=Open+Sans:wght@400;600;700&display=swap">
<style>
  :root {
    --backdrop: #ececea;
    --tallow: #cbbd9f;
    --tallow-edge: #bfb091;
    --ink-grey: #77766f;
    --ink-soft: #8e8c84;
    --ink-white: #f8f6f0;
    --card-shadow: rgba(60, 50, 30, 0.18);
  }
  * { margin: 0; padding: 0; box-sizing: border-box; }
  html, body {
    width: 1200px;
    height: 720px;
    overflow: hidden;
    background: var(--backdrop);
    font-family: "Open Sans", Arial, sans-serif;
  }
  .canvas {
    position: relative;
    width: 1200px;
    height: 720px;
  }
  .card {
    position: absolute;
    top: 205px;
    width: 540px;
    height: 309px;
    background: var(--tallow);
    border: 1px solid var(--tallow-edge);
    box-shadow: 0 6px 18px var(--card-shadow);
  }
  .card--back { left: 40px; }
  .card--front { left: 620px; }

  /* Back: contact side */
  .back-logo {
    position: absolute;
    top: 26px;
    left: 150px;
    width: 360px;
    text-align: center;
    color: var(--ink-soft);
  }
  .back-logo__name {
    font-size: 26px;
    font-weight: 400;
    letter-spacing: 0.5px;
  }
  .back-logo__tagline {
    font-size: 12px;
    margin-top: 1px;
  }
  .person {
    position: absolute;
    left: 30px;
    top: 112px;
    color: var(--ink-grey);
  }
  .person__name {
    font-size: 23px;
    font-weight: 700;
    line-height: 1.15;
  }
  .person__role {
    font-size: 17px;
    color: var(--ink-soft);
    line-height: 1.2;
  }
  .contacts {
    position: absolute;
    left: 30px;
    top: 176px;
    list-style: none;
    color: var(--ink-grey);
    font-size: 18px;
  }
  .contacts__item {
    display: flex;
    align-items: center;
    height: 29px;
  }
  .contacts__icon {
    width: 14px;
    height: 14px;
    margin-right: 10px;
    flex: none;
  }

  /* Front: logo side */
  .front-logo {
    position: absolute;
    top: 92px;
    left: 0;
    width: 100%;
    text-align: center;
    color: var(--ink-white);
  }
  .front-logo__name {
    font-size: 46px;
    font-weight: 400;
    letter-spacing: 0.5px;
    line-height: 1.1;
  }
  .front-logo__tagline {
    font-size: 22px;
    margin-top: 6px;
  }
  .front-handle {
    position: absolute;
    bottom: 18px;
    left: 0;
    width: 100%;
    text-align: center;
    color: var(--ink-white);
    font-size: 14px;
  }
</style>
</head>
<body>
<main class="canvas">

  <section class="card card--back" aria-label="Card back with contact details">
    <div class="back-logo">
      <div class="back-logo__name">Brightwater Reels</div>
      <div class="back-logo__tagline">"breathtaking wedding films"</div>
    </div>

    <div class="person">
      <div class="person__name">Paul Brightwater</div>
      <div class="person__role">producer</div>
    </div>

    <ul class="contacts">
      <li class="contacts__item">
        <svg class="contacts__icon" viewBox="0 0 14 14" aria-hidden="true">
          <circle cx="7" cy="7" r="6.2" fill="none" stroke="#77766f" stroke-width="1.4"/>
          <path d="M4.6 4.2 L5.8 4 L6.4 5.6 L5.7 6.2 Q6.4 7.6 7.8 8.3 L8.4 7.6 L10 8.2 L9.8 9.4 Q6.8 9.8 4.6 4.2 Z" fill="#77766f"/>
        </svg>
        905-418-2937
      </li>
      <li class="contacts__item">
        <svg class="contacts__icon" viewBox="0 0 14 14" aria-hidden="true">
          <circle cx="7" cy="7" r="7" fill="#77766f"/>
        </svg>
        @brightwater762
      </li>
      <li class="contacts__item">
        <svg class="contacts__icon" viewBox="0 0 14 14" aria-hidden="true">
          <rect x="1" y="3" width="12" height="8.5" rx="0.8" fill="#77766f"/>
          <path d="M1.5 3.6 L7 8 L12.5 3.6" fill="none" stroke="#cbbd9f" stroke-width="1.1"/>
        </svg>
        paul@brightwaterreels.ca
      </li>
      <li class="contacts__item">
        <svg class="contacts__icon" viewBox="0 0 14 14" aria-hidden="true">
          <circle cx="7" cy="7" r="7" fill="#77766f"/>
          <circle cx="7" cy="7" r="3.2" fill="none" stroke="#cbbd9f" stroke-width="1.2"/>
        </svg>
        www.brightwaterreels.ca
      </li>
    </ul>
  </section>

  <section class="card card--front" aria-label="Card front with name logo">
    <div class="front-logo">
      <div class="front-logo__name">Brightwater Reels</div>
      <div class="front-logo__tagline">"breathtaking wedding films"</div>
    </div>
    <div class="front-handle">@brightwater762</div>
  </section>

</main>
</body>
</html>
```